Rollup Banner & Flyer für eine Messe "Erfolg durch Innovation"

Wir benötigten für eine Messe einen Roll Up Banner und Flyer zum verteilen. Gerne basierend auf der aktuellen Firmenpräsentation und mit unseren Referenzen.
Im flyer sollen unserer Leistungen (Datenanalyse, Simulation, Optimierung und Webapplikation) dargestellt werden mit einem kleinen Text und einem aussagekräftigen bild. (https://www.kalvento.ch/leistungen/)

Target Market(s)

Industrie

Industry/Entity Type

Simulation

Font styles to use
Sans Serif
Other font styles liked:
• Roboto

Requirements
Must have
• Logo, Referenzen

```html
<!DOCTYPE html>
<html lang="de">
<head>
<meta charset="utf-8">
<title>Kalvento – Flyer &amp; Roll-up</title>
<link rel="stylesheet" href="https://fonts.googleapis.com/css2?family=Audiowide&family=Poppins:wght@400;500;600;700&family=Roboto+Condensed:wght@700&family=Roboto:wght@700&display=swap">
<style>
  :root{
    --stage:#4a4a4a;
    --black:#000;
    --lime:#dfe66a;
    --lime-soft:#cfe35a;
    --green-dark:#5d8a2b;
    --olive:#858b4e;
    --olive-text:#7c8446;
    --white:#fff;
    --silver:#d9d9d9;
  }
  *{box-sizing:border-box;margin:0;padding:0}
  html,body{width:1200px;height:3086px;overflow:hidden}
  body{background:var(--stage);position:relative;font-family:"Poppins",sans-serif;color:var(--black)}
  .abs{position:absolute}

  /* ---------- Flyer ---------- */
  .flyer{left:149px;top:183px;width:903px;height:1168px;overflow:hidden;
    background:linear-gradient(120deg,var(--lime-soft) 0%,#a6c443 45%,var(--green-dark) 100%)}
  .flyer-top{left:0;top:0;width:903px;height:352px;
    background:radial-gradient(ellipse 420px 260px at 0 0,#4a4f1c 0%,rgba(0,0,0,0) 70%),var(--black)}
  .brand{display:flex;align-items:center;gap:14px}
  .brand-dot{border-radius:50%;background:var(--lime)}
  .brand-name{font-family:"Poppins",sans-serif;font-weight:700;color:var(--lime);letter-spacing:2px}
  .flyer .brand{left:230px;top:62px}
  .flyer .brand-dot{width:70px;height:70px}
  .flyer .brand-name{font-size:56px;line-height:78px}

  .flyer-headline{left:68px;top:182px;font-family:"Audiowide",sans-serif;text-transform:uppercase}
  .flyer-headline .lead{font-size:21px;color:var(--white);line-height:26px}
  .flyer-headline .big{font-size:38px;color:var(--lime);line-height:38px}
  .flyer-divider{left:447px;top:188px;width:2px;height:88px;background:var(--white)}
  .flyer-intro{left:464px;top:184px;width:360px;font-size:15.2px;line-height:18.5px;color:var(--white)}

  .service{left:68px;width:675px;background:var(--white);border:2px solid var(--lime);border-right:none;border-radius:44px 0 0 44px}
  .service-shade{right:0;top:-2px;bottom:-2px;width:157px;background:var(--black)}
  .service-title{left:40px;font-family:"Roboto Condensed",sans-serif;font-weight:700;font-size:25px;color:var(--olive-text)}
  .service-text{left:42px;width:465px;font-size:12.6px;line-height:14.5px;color:#111}
  .pill{height:34px;width:158px;border-radius:17px;color:var(--white);font-family:"Roboto",sans-serif;font-weight:700;font-size:17px;display:flex;align-items:center;justify-content:center}
  .pill.olive{background:var(--olive)}
  .pill.dark{background:var(--black)}

  .monitor{width:182px}
  .monitor-bezel{width:182px;height:138px;background:#111;border:3px solid #2a2a2a;border-radius:4px;padding:6px}
  .monitor-screen{width:100%;height:100%;background:linear-gradient(180deg,#f4f4f4,#d7dde2)}
  .monitor-chin{width:182px;height:14px;background:linear-gradient(#f2f2f2,#bdbdbd);border-radius:0 0 4px 4px}
  .monitor-neck{margin:0 auto;width:46px;height:18px;background:linear-gradient(90deg,#bbb,#eee,#bbb)}
  .monitor-foot{margin:0 auto;width:110px;height:8px;background:#d0d0d0;border-radius:50%}

  .contact-row{left:68px;top:1090px;width:760px;display:flex;justify-content:space-between;font-size:24px;font-weight:500;color:var(--white)}
  .contact-item{display:flex;align-items:center;gap:8px}
  .contact-icon{width:26px;height:26px;border-radius:50%;background:var(--black);display:flex;align-items:center;justify-content:center}

  /* ---------- Roll-up ---------- */
  .rollup{left:251px;top:1481px;width:699px;height:1397px;overflow:hidden;
    background:radial-gradient(ellipse 380px 300px at 0 0,#4a4f1c 0%,rgba(0,0,0,0) 70%),var(--black)}
  .rollup .brand{left:153px;top:58px}
  .rollup .brand-dot{width:80px;height:80px}
  .rollup .brand-name{font-size:60px;line-height:80px}
  .rollup-panel{left:57px;top:187px;width:586px;height:1000px;background:var(--white);border-radius:60px 60px 0 0}
  .rollup-head{left:57px;width:586px;text-align:center;font-family:"Audiowide",sans-serif;text-transform:uppercase}
  .rollup-head.lead{top:222px;font-size:34px;line-height:34px}
  .rollup-head.big{top:296px;font-size:53px;line-height:52px;color:var(--olive-text)}
  .dots{left:0;width:699px;top:411px;display:flex;justify-content:center;gap:4px}
  .dots span{width:11px;height:11px;border-radius:50%;background:var(--olive)}
  .dots span:nth-child(n+6){background:var(--lime-soft)}
  .rollup-intro{left:120px;width:460px;top:445px;text-align:center;font-size:18.5px;line-height:21px}

  .row-bar{height:65px;background:var(--olive);color:var(--white);font-family:"Roboto Condensed",sans-serif;font-weight:700;font-size:31px;display:flex;align-items:center;white-space:nowrap}
  .row-bar.left{left:140px;width:388px;border-radius:0 33px 33px 0;padding-left:80px}
  .row-bar.right{left:170px;width:390px;border-radius:33px 0 0 33px;justify-content:flex-end;padding-right:86px}
  .row-icon{width:110px;height:110px;border-radius:50%;background:var(--black);border:7px solid var(--lime);display:flex;align-items:center;justify-content:center}

  .rollup-wave{left:0;top:1040px;width:699px;height:357px}
  .rollup .monitor{left:165px;top:929px;width:355px}
  .rollup .monitor-bezel{width:355px;height:212px;padding:8px}
  .rollup .monitor-chin{width:355px;height:0}
  .rollup .monitor-neck{width:70px;height:40px}
  .rollup .monitor-foot{width:170px;height:14px}
  .plant{width:90px;height:100px;border-radius:50% 50% 10px 10px;background:radial-gradient(ellipse at 50% 60%,#2f5a1e,#17330e)}

  .rollup-phone{left:0;width:699px;top:1226px;display:flex;justify-content:center;align-items:center;gap:14px;font-weight:700;font-size:52px;color:var(--white);line-height:60px}
  .rollup-phone .contact-icon{width:48px;height:48px}
  .url-bar{left:57px;top:1300px;width:583px;height:60px;border-radius:30px;background:var(--black);border:3px solid var(--lime);display:flex;align-items:center;justify-content:center;font-family:"Audiowide",sans-serif;font-size:32px;letter-spacing:14px;color:var(--white)}
  .url-bar .accent{color:var(--lime)}
</style>
</head>
<body>

<!-- Flyer -->
<section class="flyer abs">
  <div class="flyer-top abs"></div>
  <div class="brand abs"><span class="brand-dot"></span><span class="brand-name">KALVENTO</span></div>

  <div class="flyer-headline abs">
    <div class="lead">Du hast eine schwierige</div>
    <div class="big">Entscheidung</div>
    <div class="big">zu treffen?</div>
  </div>
  <div class="flyer-divider abs"></div>
  <p class="flyer-intro abs">Was wäre, wenn wir dir zeigen würden, welche Option die Beste ist? Wir unterstützen Unternehmen in Logistik und Produktion die besten Entscheidungen zu treffen und dass innerhalb weniger Wochen.</p>

  <!-- Daten-analyse -->
  <article class="service abs" style="top:301px;height:163px">
    <div class="service-shade abs"></div>
    <h3 class="service-title abs" style="top:38px">Daten-analyse</h3>
    <p class="service-text abs" style="top:82px">Datenanalyse macht Prozesse sichtbar, erkennt Muster und schafft eine objektive Grundlage für Entscheidungen. Wir strukturieren, bereinigen und analysieren Daten so, dass sie einen echten Nutzen erzeugen.</p>
  </article>
  <div class="pill olive abs" style="left:53px;top:441px">Transparent</div>
  <div class="pill dark abs" style="left:227px;top:441px">Verständlich</div>
  <div class="pill olive abs" style="left:403px;top:441px">Aussagekräftig</div>
  <div class="monitor abs" style="left:630px;top:293px">
    <div class="monitor-bezel"><div class="monitor-screen" role="img" aria-label="Bildschirmansicht einer Datenanalyse mit Karte und Balkendiagramm"></div></div>
    <div class="monitor-chin"></div><div class="monitor-neck"></div><div class="monitor-foot"></div>
  </div>

  <!-- Simulation -->
  <article class="service abs" style="top:505px;height:150px">
    <div class="service-shade abs"></div>
    <h3 class="service-title abs" style="top:20px">Simulation</h3>
    <p class="service-text abs" style="top:60px">Simulation bildet reale Prozesse digital ab, damit Abläufe, Kapazitäten und Varianten risikofrei getestet werden können.</p>
  </article>
  <div class="pill olive abs" style="left:53px;top:614px">Vergleichbar</div>
  <div class="pill dark abs" style="left:227px;top:614px">Belastbar</div>
  <div class="pill olive abs" style="left:403px;top:614px">Risikoarm</div>
  <div class="monitor abs" style="left:630px;top:469px">
    <div class="monitor-bezel"><div class="monitor-screen" role="img" aria-label="Bildschirmansicht einer Simulation mit Landkarte"></div></div>
    <div class="monitor-chin"></div><div class="monitor-neck"></div><div class="monitor-foot"></div>
  </div>

  <!-- Optimierung -->
  <article class="service abs" style="top:679px;height:178px">
    <div class="service-shade abs"></div>
    <h3 class="service-title abs" style="top:22px">Optimierung</h3>
    <p class="service-text abs" style="top:62px">Optimierung sucht automatisch nach der besten Lösung – sei es bei Planung, Ressourcen, Routen oder Abläufen. Mit Algorithmen und intelligenten Modellen finden wir Varianten, die Kosten senken, Kapazitäten besser nutzen und Entscheidungen beschleunigen.</p>
  </article>
  <div class="pill olive abs" style="left:53px;top:815px">Efficent</div>
  <div class="pill dark abs" style="left:227px;top:815px">Zielgerichtet</div>
  <div class="pill olive abs" style="left:403px;top:815px">Robust</div>
  <div class="monitor abs" style="left:630px;top:672px">
    <div class="monitor-bezel"><div class="monitor-screen" role="img" aria-label="Bildschirmansicht einer Einsatzplanung mit Gantt-Balken"></div></div>
    <div class="monitor-chin"></div><div class="monitor-neck"></div><div class="monitor-foot"></div>
  </div>

  <!-- Web-applikationen -->
  <article class="service abs" style="top:882px;height:177px">
    <div class="service-shade abs"></div>
    <h3 class="service-title abs" style="top:20px">Web-applikationen</h3>
    <p class="service-text abs" style="top:60px">Wir entwickeln individuelle Webapplikationen, die Daten, Simulationen und Optimierungen in einem benutzerfreundlichen Tool zusammenführen. So entstehen Lösungen, die direkt im Alltag genutzt werden – einfach, schnell und ohne Installation.</p>
  </article>
  <div class="pill olive abs" style="left:53px;top:1015px">Zugänglich</div>
  <div class="pill dark abs" style="left:227px;top:1015px">Verfugtbar</div>
  <div class="pill olive abs" style="left:403px;top:1015px">Flexibel</div>
  <div class="monitor abs" style="left:632px;top:879px">
    <div class="monitor-bezel"><div class="monitor-screen" role="img" aria-label="Bildschirmansicht einer Webapplikation mit Dashboard"></div></div>
    <div class="monitor-chin"></div><div class="monitor-neck"></div><div class="monitor-foot"></div>
  </div>

  <div class="contact-row abs">
    <span class="contact-item"><span class="contact-icon"><svg width="14" height="14" viewBox="0 0 24 24"><path fill="#fff" d="M6.6 10.8a15 15 0 0 0 6.6 6.6l2.2-2.2c.3-.3.7-.4 1-.2 1.1.4 2.3.6 3.6.6.6 0 1 .4 1 1V20c0 .6-.4 1-1 1A17 17 0 0 1 3 4c0-.6.4-1 1-1h3.5c.6 0 1 .4 1 1 0 1.3.2 2.5.6 3.6.1.3 0 .7-.2 1z"/></svg></span>+41 81 000 12 34</span>
    <span class="contact-item"><span class="contact-icon"><svg width="14" height="14" viewBox="0 0 24 24"><path fill="#fff" d="M3 5h18v14H3z"/><path fill="none" stroke="#000" stroke-width="2" d="M3 6l9 7 9-7"/></svg></span>info@kalvento.ch</span>
    <span class="contact-item"><span class="contact-icon"><svg width="16" height="16" viewBox="0 0 24 24"><circle cx="12" cy="12" r="9" fill="none" stroke="#fff" stroke-width="2"/><path fill="none" stroke="#fff" stroke-width="2" d="M3 12h18M12 3c3 3 3 15 0 18M12 3c-3 3-3 15 0 18"/></svg></span>www.kalvento.ch</span>
  </div>
</section>

<!-- Roll-up -->
<section class="rollup abs">
  <div class="brand abs"><span class="brand-dot"></span><span class="brand-name">KALVENTO</span></div>

  <div class="rollup-panel abs"></div>
  <div class="rollup-head lead abs">Du hast eine<br>schwierige</div>
  <div class="rollup-head big abs">Entscheidung<br>zu treffen?</div>
  <div class="dots abs"><span></span><span></span><span></span><span></span><span></span><span></span><span></span></div>
  <p class="rollup-intro abs">Was wäre, wenn wir dir zeigen würden, welche Option die Beste ist? Wir unterstützen Unternehmen in Logistik und Produktion die besten Entscheidungen zu treffen und dass innerhalb weniger Wochen.</p>

  <div class="row-bar left abs" style="top:575px">Daten-analyse</div>
  <div class="row-icon abs" style="left:95px;top:553px"><svg width="56" height="56" viewBox="0 0 56 56"><g fill="var(--lime)"><rect x="6" y="36" width="6" height="14"/><rect x="15" y="30" width="6" height="20"/><rect x="24" y="24" width="6" height="26"/></g><circle cx="34" cy="20" r="11" fill="none" stroke="var(--lime)" stroke-width="4"/><path d="M42 28l10 10" stroke="var(--lime)" stroke-width="5"/></svg></div>

  <div class="row-bar right abs" style="top:658px">Simulation</div>
  <div class="row-icon abs" style="left:498px;top:633px"><svg width="52" height="52" viewBox="0 0 52 52"><rect x="8" y="10" width="36" height="26" fill="none" stroke="var(--lime)" stroke-width="4"/><circle cx="26" cy="23" r="7" fill="var(--lime)"/><rect x="10" y="40" width="32" height="5" fill="var(--lime)"/></svg></div>

  <div class="row-bar left abs" style="top:740px">Optimierung</div>
  <div class="row-icon abs" style="left:95px;top:717px"><svg width="54" height="54" viewBox="0 0 54 54"><circle cx="27" cy="27" r="13" fill="none" stroke="var(--lime)" stroke-width="8" stroke-dasharray="6 4"/><circle cx="27" cy="27" r="5" fill="var(--lime)"/><path d="M27 27L46 8" stroke="var(--lime)" stroke-width="4"/><path d="M38 6h10v10" fill="none" stroke="var(--lime)" stroke-width="4"/></svg></div>

  <div class="row-bar right abs" style="top:823px">Web-applikationen</div>
  <div class="row-icon abs" style="left:498px;top:801px"><svg width="54" height="54" viewBox="0 0 54 54"><g stroke="var(--lime)" stroke-width="3"><path d="M27 27L10 12M27 27L44 12M27 27L8 32M27 27L46 32"/></g><g fill="var(--lime)"><circle cx="10" cy="12" r="5"/><circle cx="44" cy="12" r="5"/><circle cx="8" cy="32" r="5"/><circle cx="46" cy="32" r="5"/><rect x="16" y="26" width="22" height="22" rx="6"/></g></svg></div>

  <svg class="rollup-wave abs" viewBox="0 0 699 357" preserveAspectRatio="none" aria-hidden="true">
    <defs><linearGradient id="rollupGreen" x1="0" y1="0" x2="1" y2="1"><stop offset="0" stop-color="#cfe35a"/><stop offset="0.5" stop-color="#9cbf40"/><stop offset="1" stop-color="#5d8a2b"/></linearGradient></defs>
    <path d="M0 50 Q350 -40 699 50 V357 H0Z" fill="#000"/>
    <path d="M0 60 Q350 -20 699 60 V357 H0Z" fill="url(#rollupGreen)"/>
  </svg>

  <div class="plant abs" role="img" aria-label="Grünpflanze links neben dem Bildschirm" style="left:70px;top:1000px"></div>
  <div class="plant abs" role="img" aria-label="Grünpflanze rechts neben dem Bildschirm" style="left:515px;top:1000px"></div>

  <div class="monitor abs">
    <div class="monitor-bezel"><div class="monitor-screen" role="img" aria-label="Bildschirmansicht eines Analytics-Dashboards mit Diagrammen"></div></div>
    <div class="monitor-chin"></div><div class="monitor-neck"></div><div class="monitor-foot"></div>
  </div>

  <div class="rollup-phone abs"><span class="contact-icon"><svg width="24" height="24" viewBox="0 0 24 24"><path fill="#fff" d="M6.6 10.8a15 15 0 0 0 6.6 6.6l2.2-2.2c.3-.3.7-.4 1-.2 1.1.4 2.3.6 3.6.6.6 0 1 .4 1 1V20c0 .6-.4 1-1 1A17 17 0 0 1 3 4c0-.6.4-1 1-1h3.5c.6 0 1 .4 1 1 0 1.3.2 2.5.6 3.6.1.3 0 .7-.2 1z"/></svg></span>+41 81 000 12 34</div>
  <div class="url-bar abs">WWW.<span class="accent">KALVENTO</span>.CH</div>
</section>

</body>
</html>
```